Design Packaging Labels for GlossaTrin 417

Redesign current label. I would like a 4 x 6 inch label that is in our colors (see glossatrin.com) . I do not want a white label as the bottle is white. The product name is GlossaTrin 417. This product is a coating like a paint. The purpose of the label is to provide user information and to comply with safety regulations. We also would like a little bit of marketing as you can see by the product description and introduction in the word document provided. This product will be sold to professional applicators.

Target Market(s)

Business (construction and coatings)

Industry/Entity Type

Paint

Font styles to use
Sans Serif

Colors

Designer to choose colors to be used in the design.

Requirements
Must have
• All safety placards and warnings
Should not have
• Not be a white label

```html
<!DOCTYPE html>
<html lang="en">
<head>
<meta charset="utf-8">
<title>GlossaTrin 417 Label</title>
<link rel="stylesheet" href="https://fonts.googleapis.com/css2?family=Figtree:wght@400;500;600&family=Oswald:wght@500&display=swap">
<style>
  :root {
    --teal: #5fb8a5;
    --teal-light: #8fd4c5;
    --ink: #121212;
    --ink-2: #1e1e1e;
    --white: #ffffff;
    --grey: #9a9a9a;
    --canvas: #ececec;
    --hazard-red: #e3262b;
  }
  * { margin: 0; padding: 0; box-sizing: border-box; }
  html, body { width: 1200px; height: 938px; overflow: hidden; }
  body { background: var(--canvas); font-family: "Figtree", sans-serif; color: var(--white); position: relative; }

  .label {
    position: absolute; left: 61px; top: 104px; width: 1084px; height: 722px;
    background: repeating-linear-gradient(135deg, var(--ink) 0 3px, var(--ink-2) 3px 5px);
    overflow: hidden;
  }
  .label__band {
    position: absolute; left: 0; top: 0; width: 153px; height: 100%;
    background: linear-gradient(180deg, var(--teal), var(--teal-light));
  }
  .label__frame {
    position: absolute; left: 18px; top: 14px; right: 17px; bottom: 14px;
    border: 3px solid var(--white); border-radius: 32px;
  }
  .label__product-name {
    position: absolute; left: 87px; top: 361px;
    transform: translate(-50%, -50%) rotate(-90deg);
    font-family: "Oswald", sans-serif; font-weight: 500;
    font-size: 96px; line-height: 1; letter-spacing: 1px; white-space: nowrap;
    color: var(--white); text-transform: uppercase;
  }

  .brand { position: absolute; left: 300px; top: 98px; width: 302px; display: flex; align-items: center; justify-content: center; gap: 14px; }
  .brand__dot { width: 28px; height: 28px; border-radius: 50%; background: var(--teal-light); }
  .brand__name { font-size: 48px; font-weight: 500; color: var(--grey); letter-spacing: 1px; line-height: 1; }

  .info { position: absolute; left: 203px; width: 492px; font-size: 14px; line-height: 18px; }
  .heading { color: var(--teal); font-weight: 500; font-size: 14px; text-transform: uppercase; }
  .info--description { top: 232px; }
  .info--characteristics { top: 340px; }
  .info--handling { top: 523px; }
  .features { list-style: none; }
  .features li { position: relative; padding-left: 12px; }
  .features li::before { content: ""; position: absolute; left: 1px; top: 8px; width: 3px; height: 3px; border-radius: 50%; background: var(--teal); }

  .maker { position: absolute; left: 208px; top: 634px; }
  .maker__name { font-size: 30px; font-weight: 500; color: var(--teal-light); line-height: 1; }
  .maker__sub { font-size: 10px; letter-spacing: 3px; color: var(--grey); text-transform: uppercase; margin-top: 4px; }
  .address { position: absolute; left: 446px; top: 640px; font-size: 14px; line-height: 18px; font-weight: 600; font-style: normal; color: var(--teal); text-transform: uppercase; }

  .safety {
    position: absolute; left: 750px; top: 55px; width: 284px; height: 615px;
    border: 2px solid var(--teal); padding: 20px 20px 0 22px; font-size: 13px; line-height: 18px;
  }
  .safety .heading { font-size: 13px; }
  .safety__signal { font-size: 19px; line-height: 24px; margin-bottom: 10px; }
  .safety__signal span { color: var(--teal-light); }
  .safety p { margin-bottom: 12px; }
  .pictograms { position: absolute; left: 18px; bottom: 10px; display: flex; gap: 8px; }
  .pictogram { width: 76px; height: 76px; }
</style>
</head>
<body>
  <div class="label">
    <div class="label__band"></div>
    <div class="label__frame"></div>
    <div class="label__product-name">GlossaTrin 417</div>

    <div class="brand">
      <div class="brand__dot"></div>
      <div class="brand__name">GlossaTrin</div>
    </div>

    <section class="info info--description">
      <h2 class="heading">Product Description:</h2>
      <p>GT.417 is a transparent, ready-to-use coating for protecting non-absorbent surfaces from corrosion and graffiti. Based on patented polysilazane nano-technology, it produces a permanent protective layer that covalently bonds to the substrate and hardens at room temperature.</p>
    </section>

    <section class="info info--characteristics">
      <h2 class="heading">Characteristics:</h2>
      <ul class="features">
        <li>Exceptional corrosion protection</li>
        <li>Easy to clean</li>
        <li>Excellent substrate adhesion</li>
        <li>Weather-resistant</li>
        <li>High UV and chemical resistant</li>
        <li>Easy to apply</li>
        <li>Hardens at room temperature</li>
        <li>21 fluid ounces</li>
      </ul>
    </section>

    <section class="info info--handling">
      <h2 class="heading">Handling and Storage:</h2>
      <p>Keep only in original container. Absolutely not to be handled by children. Do not keep in temperatures above 10°C. Open the container periodically to release potential built-up pressure (ammonia gas). Container to be kept tightly closed in a dry, well-ventilated place.</p>
    </section>

    <div class="maker">
      <div class="maker__name">Corvel</div>
      <div class="maker__sub">Applied Science</div>
    </div>
    <address class="address">418 Harbor Lane, Suite 22<br>Port Wren, Oregon 97999</address>

    <aside class="safety">
      <div class="safety__signal">Signal Word: <span>Danger</span></div>
      <p><span class="heading">Contains:</span> dibutyl ether (142-96-1); Polysilzane (90387-00-1). The following percentage of the mixture consists of ingredient(s) with unknown hazards to the aquatic environment: 1%</p>
      <p><span class="heading">Hazard Statements:</span> Highly flammable liquid and vapor. Harmful if swallowed. Causes severe skin burns and eye damage. May cause drowsiness or dizziness. Harmful to aquatic life with long lasting effects.</p>
      <p><span class="heading">Precautionary Statements:</span> Keep away from heat/sparks/open flames/ hot surfaces. No smoking. IF ON SKIN (or hair): Remove/ Take off all contaminated clothing immediately and rinse skin with water/ shower. IF IN EYES rinse cautiously with water for several minutes. Remove contact lenses, if present and easy to do. Continue rinsing. Refer to attached safety data sheets and/or instructions for use.</p>

      <div class="pictograms">
        <svg class="pictogram" viewBox="0 0 76 76" role="img" aria-label="Flammable hazard pictogram">
          <rect x="14" y="14" width="48" height="48" transform="rotate(45 38 38)" fill="#fff" stroke="var(--hazard-red)" stroke-width="5"/>
          <rect x="28" y="26" width="20" height="24" fill="#cfcfcf"/>
        </svg>
        <svg class="pictogram" viewBox="0 0 76 76" role="img" aria-label="Corrosive hazard pictogram">
          <rect x="14" y="14" width="48" height="48" transform="rotate(45 38 38)" fill="#fff" stroke="var(--hazard-red)" stroke-width="5"/>
          <rect x="24" y="28" width="28" height="20" fill="#cfcfcf"/>
        </svg>
        <svg class="pictogram" viewBox="0 0 76 76" role="img" aria-label="Irritant hazard pictogram">
          <rect x="14" y="14" width="48" height="48" transform="rotate(45 38 38)" fill="#fff" stroke="var(--hazard-red)" stroke-width="5"/>
          <path d="M34 21h8l-2 24h-4z" fill="#111"/>
          <circle cx="38" cy="52" r="4" fill="#111"/>
        </svg>
      </div>
    </aside>
  </div>
</body>
</html>
```